Trifold Leaflet - Osteopathy

Trifold Leaflet (A4 size paper) to provide information and promote an established English seafront osteopathy clinic.
I would like a simple modern design to reflect the seafront location and the caring nature of osteopathy treatment. The design needs to be not be generic or too corporate.
At the top of the front page in a large font should be the word "Osteopathy" as it will be displayed in a rack of leaflets (photo attached) and needs to be eye-catching.
I have attached a logo file and some examples of the kinds of designs that I like- but i'm very open to your expert ideas!
Also attached is a photo of the location- a bit of an ugly building but right on the beach, it would be great if this location could be emphasized!
The Word files: Leaflets word-inside.doc & Leaflets word-outside.doc uploaded show the content that I'd like- this is definitely not set in stone and I appreciate that less content is probably needed. Feel free to include/leave out whatever you feel is right.
More info on the practice can be found on my website:
www.harbourlinespine.com
The shutterstock images are ones that I have previously bought the rights to use, but only use them if you think they suit you design- I have included them i case they are of use to you.
Any adult.
Building

```html
<!DOCTYPE html>
<html lang="en">
<head>
<meta charset="utf-8">
<title>Harbourline Osteopathy – Trifold Leaflet</title>
<link rel="stylesheet" href="https://fonts.googleapis.com/css2?family=Mulish:wght@400;600;800;900&display=swap">
<style>
  :root{
    --page-bg:#e4e4e4;
    --white:#ffffff;
    --steel-light:#8b8b8b;
    --steel-mid:#6f6f6f;
    --steel-dark:#4a4a4a;
    --ink:#1e1e1e;
    --ink-soft:#3b3b3b;
    --red:#c8493a;
    --navy:#243a66;
    --pale:#f0f0f0;
  }
  *{box-sizing:border-box;margin:0;padding:0}
  html,body{width:1200px;height:1000px;overflow:hidden;background:var(--page-bg);font-family:"Mulish",sans-serif}
  .leaflet{position:absolute;left:75px;top:129px;width:1050px;height:742px;display:flex;box-shadow:0 6px 24px rgba(0,0,0,.18)}
  .panel{position:relative;width:350px;height:742px;overflow:hidden;
    background:linear-gradient(160deg,var(--steel-light),var(--steel-mid) 55%,#7c7c7c)}
  .panel + .panel{border-left:1px solid rgba(0,0,0,.12)}

  /* left panel */
  .brand-strip{position:absolute;left:0;top:0;width:350px;height:92px;background:var(--white)}
  .brand{position:absolute;right:26px;top:30px;display:flex;align-items:center;gap:8px;
    font-weight:600;font-size:17px;color:var(--red)}
  .brand-dot{width:10px;height:10px;border-radius:50%;background:var(--red)}
  .intro{position:absolute;left:0;top:92px;width:350px;height:250px;background:var(--steel-dark);
    clip-path:polygon(0 0,100% 0,100% 78%,82% 100%,0 100%);padding:20px 30px 0 28px;
    color:var(--pale);font-size:12px;line-height:1.5}
  .pill{position:absolute;left:70px;top:358px;background:var(--white);color:var(--ink-soft);
    font-weight:800;font-size:14.5px;padding:6px 16px;border-radius:4px}
  .treating{position:absolute;left:175px;top:410px;color:var(--white)}
  .treating h2{font-weight:900;font-size:27px;margin-bottom:6px}
  .treating li{list-style:none;font-weight:800;font-size:14.5px;line-height:1.55}
  .anatomy{position:absolute;left:38px;top:420px;width:120px;height:290px;border-radius:50px 50px 20px 20px;
    background:linear-gradient(180deg,#c9a79c,#a85a4c 55%,#8e4a40)}
  .leader{position:absolute;left:0;top:0}

  /* middle panel */
  .treatment-photo{position:absolute;left:0;top:0;width:350px;height:440px;
    background:linear-gradient(170deg,#f4f2ef,#d9d4ce 45%,#b7aba1 75%,#e9e6e2);
    clip-path:polygon(0 0,100% 0,100% 86%,50% 100%,0 86%)}
  .endorse{position:absolute;left:30px;top:452px;width:295px;color:var(--white)}
  .endorse .lead{font-size:14px}
  .endorse h3{font-weight:900;font-size:19px;margin:2px 0 10px}
  .endorse p{font-size:11.5px;line-height:1.5;color:var(--pale)}
  .badges{position:absolute;left:38px;top:650px;display:flex;align-items:center;gap:22px}
  .badge-square{width:38px;height:38px;border:2px solid var(--ink-soft)}
  .badge-round{width:48px;height:34px;border:2px solid var(--ink-soft);border-radius:50%}
  .badge-navy{width:62px;height:62px;background:var(--navy);margin-left:46px}

  /* right panel */
  .regulated{position:absolute;left:0;top:0;width:350px;height:330px;background:var(--white);
    clip-path:polygon(0 0,100% 0,100% 80%,0 100%);padding:56px 28px 0 30px}
  .regulated h1{font-weight:900;font-size:36px;letter-spacing:.5px;color:var(--ink);line-height:1}
  .regulated .sub{font-size:17px;color:var(--red);margin-top:2px}
  .regulated .safe{font-size:52px;font-weight:400;color:var(--ink);line-height:1;letter-spacing:1px}
  .regulated .safe span{color:var(--red);font-size:68px;vertical-align:-6px}
  .regulated p{font-size:10.5px;line-height:1.45;color:var(--ink-soft);margin-top:6px;width:220px}
  .hands-photo{position:absolute;right:18px;top:272px;width:104px;height:104px;border-radius:50%;
    border:4px solid var(--pale);background:radial-gradient(circle at 45% 45%,#d8b7a3,#9a7766 60%,#4d3d37)}
  .first-visit{position:absolute;left:22px;top:382px;width:310px;color:var(--ink)}
  .first-visit h2{font-weight:900;font-size:24px;line-height:1.2;margin-bottom:2px}
  .first-visit h4{font-weight:900;font-size:12.5px;line-height:1.25;margin-top:5px}
  .first-visit p{font-size:9.8px;line-height:1.28;font-weight:600}
  .cta{position:absolute;left:22px;bottom:10px;width:306px;background:var(--red);border-radius:14px;
    padding:7px 16px;color:var(--white);text-align:right}
  .cta .note{font-size:11px;line-height:1.2}
  .cta .call{font-weight:800;font-size:18px;line-height:1.2;letter-spacing:1px;display:flex;justify-content:flex-end;align-items:center;gap:8px;margin-top:3px}
</style>
</head>
<body>
<main class="leaflet">
  <section class="panel panel-about">
    <div class="brand-strip">
      <div class="brand"><span class="brand-dot"></span>Harbourline Osteopathy</div>
    </div>
    <div class="intro">
      Much of the pain and disability we suffer stems from abnormalities in our body's structure and function. Osteopathy treats problems related to the musculoskeletal system: muscles, ligaments, nerves and joints, and helps the body's natural healing ability to correct itself and relieve the pain caused by dysfunction. When the body is balanced and efficient, just like a tuned engine, it will function with minimum wear and tear, requiring less energy to operate correctly.
    </div>
    <div class="pill">Natural, Drug Free, Pain Relief</div>
    <div class="anatomy" role="img" aria-label="Anatomical illustration of a human figure showing muscles and skeleton with pain areas highlighted"></div>
    <svg class="leader" width="350" height="742" aria-hidden="true">
      <g stroke="#e6e6e6" stroke-width="1" stroke-dasharray="2 3" fill="none">
        <path d="M120 470 L172 456"/>
        <path d="M135 530 L172 478"/>
        <path d="M110 455 L172 500"/>
        <path d="M140 560 L172 522"/>
        <path d="M125 620 L172 544"/>
      </g>
    </svg>
    <div class="treating">
      <h2>Treating:</h2>
      <ul>
        <li>Back &amp; Neck Pain</li>
        <li>Arthritis &amp; Joint Pain</li>
        <li>Frozen Shoulder</li>
        <li>Sciatica</li>
        <li>Sports Injury</li>
      </ul>
    </div>
  </section>

  <section class="panel panel-endorse">
    <div class="treatment-photo" role="img" aria-label="Photograph of an osteopath treating a patient's shoulder on a treatment couch"></div>
    <div class="endorse">
      <div class="lead">As Recommended by</div>
      <h3>The National Practice Guild</h3>
      <p>Osteopathy is used to treat many problems related to the musculoskeletal system. Osteopathic manipulation has been recommended by the National Clinical Guidance Board (NCGB) and The National Practice Guild (NPG) for the treatment of low back pain.</p>
    </div>
    <div class="badges">
      <div class="badge-square"></div>
      <div class="badge-round"></div>
      <div class="badge-navy"></div>
    </div>
  </section>

  <section class="panel panel-visit">
    <div class="regulated">
      <h1>OSTEOPATHY</h1>
      <div class="sub">is Regulated</div>
      <div class="safe">SAFE<span>&amp;</span></div>
      <p>Osteopathy is one of only two complementary and alternative medicines (CAMs) that are regulated under UK law. This regulation works in much the same way as regulation for medical doctors.</p>
    </div>
    <div class="hands-photo" role="img" aria-label="Close-up photograph of hands massaging a shoulder"></div>
    <div class="first-visit">
      <h2>Your first visit</h2>
      <h4>Medical History</h4>
      <p>On your first visit we will ask you lots of questions to build up a detailed medical history. Your past medical history can often be relevant to current problems you are experiencing. We may ask about past illnesses, operations, injuries, accidents and medications.</p>
      <h4>Assessment</h4>
      <p>Based on your medical history, we will perform some tests to help form a diagnosis of your current condition. Typical tests include range and quality of joint movements, tenderness to palpation, muscle tone and strength, reflexes and blood pressure.</p>
      <h4>Treatment</h4>
      <p>Supported by in depth knowledge of anatomy and physiology, the examination enables the Osteopath to diagnose accurately and choose the right treatment. Treatment involves gentle, manual techniques – easing pain, reducing swelling and improving mobility.</p>
    </div>
    <div class="cta">
      <div class="note">For further information<br>or if you have any questions</div>
      <div class="call">CALL
        <svg width="20" height="20" viewBox="0 0 24 24" aria-hidden="true"><circle cx="12" cy="12" r="11" fill="none" stroke="#fff" stroke-width="2"/><path d="M8.5 6.5l2 2-1.2 1.6c.8 1.8 2 3 3.6 3.8l1.6-1.2 2 2-1.6 1.8c-3.8-.6-7.4-4.2-8-8z" fill="#fff"/></svg>
        01632 960418</div>
    </div>
  </section>
</main>
</body>
</html>
```